Quelmira Nutraceuticals Product Label

Quelmira corporation (quel-mi-ra - "to yourhealth") is a healthcare and wellness company in Los Angeles. We produce a line of vitamins/nutritional supplements under brand name QuelStrida ( to your progress) and a line of skincare products or creams under the brand name QuelNuvio ( to your dreams). We already have logos designed for quelmira, quelnuvio, and quelstrida which are very similar, and our products can be found in tradewick.com under these brands as well as at www.drpetravik.com, www.quelmira.com. Our tag line has been "Health built on evidence"
I am looking to recreate a branding look for our vitamins which can make them appear more vibrant and modern and exciting , while maintaining the air of scientific authority we aimed at before. We want to be able to extend the format to our skin- care line in the future . The skin care line will be sold in upscale stores around the world as well as on the web.
This project requires a new design label for our vitamin products. I will attach appropriate logo files and photos of our vitamins as they are now. They come in white vitamin bottles. The Label wraps around the bottle. The center panel includes the artwork and logos and is bordered on left and right by panels that carry product information. Files attached are self-explanatory. Please email me if you need more direction or info.
Healthcare

```html
<!DOCTYPE html>
<html lang="en">
<head>
<meta charset="utf-8">
<title>QuelStrida Stress Formula Labels</title>
<link rel="stylesheet" href="https://fonts.googleapis.com/css2?family=Questrial&display=swap">
<style>
  :root {
    --teal: #1b7e93;
    --teal-deep: #14697c;
    --teal-text: #1d7f96;
    --orange: #f07a21;
    --band-light: #c7e5ea;
    --band-light-edge: #e6f4f6;
    --band-grey: #a9c0c5;
    --band-grey-edge: #c9d9dc;
    --ink: #12333b;
    --grey: #505a5d;
    --muted: #8a9497;
    --paper: #ffffff;
    --backdrop: #f1f3f4;
  }
  * { margin: 0; padding: 0; box-sizing: border-box; }
  html, body { width: 1200px; height: 1004px; overflow: hidden; }
  body {
    background: var(--backdrop);
    font-family: "Questrial", "Century Gothic", sans-serif;
    display: flex;
    align-items: center;
    justify-content: center;
    gap: 40px;
  }
  .label {
    width: 540px;
    height: 760px;
    background: var(--paper);
    display: flex;
    flex-direction: column;
    align-items: center;
    box-shadow: 0 2px 10px rgba(0,0,0,0.08);
  }
  .brand-header {
    margin-top: 26px;
    width: 86%;
    height: 200px;
    background: linear-gradient(180deg, var(--teal) 0%, var(--teal-deep) 100%);
    display: flex;
    flex-direction: column;
    align-items: center;
    justify-content: center;
    color: var(--paper);
  }
  .brand-mark {
    width: 30px;
    height: 30px;
    border-radius: 50%;
    background: var(--paper);
    margin-bottom: 14px;
  }
  .brand-name {
    font-size: 50px;
    letter-spacing: 1px;
    line-height: 1;
  }
  .brand-tagline {
    margin-top: 12px;
    font-size: 13px;
    letter-spacing: 2.5px;
    text-transform: uppercase;
  }
  .header-rule { width: 86%; height: 5px; background: var(--orange); }
  .rule-orange { width: 100%; height: 4px; background: var(--orange); }
  .product-name {
    margin-top: 16px;
    text-align: center;
    line-height: 0.95;
    text-transform: uppercase;
    font-weight: 400;
  }
  .product-name .word-stress { display: block; font-size: 88px; color: var(--orange); }
  .product-name .word-formula { display: block; font-size: 92px; color: var(--teal-text); }
  .claim-band {
    margin-top: 16px;
    width: 100%;
    height: 90px;
    display: flex;
    flex-direction: column;
    align-items: center;
    justify-content: center;
    color: var(--ink);
    background: linear-gradient(90deg, var(--band-light-edge), var(--band-light) 30%, var(--band-light) 70%, var(--band-light-edge));
  }
  .label.alt .claim-band {
    background: linear-gradient(90deg, var(--band-grey-edge), var(--band-grey) 25%, var(--band-grey) 75%, var(--band-grey-edge));
  }
  .claim-title { font-size: 28px; text-transform: uppercase; }
  .claim-detail { font-size: 20px; margin-top: 4px; }
  .panel-note {
    width: 100%;
    text-align: center;
    font-size: 13px;
    letter-spacing: 1px;
    text-transform: uppercase;
    color: var(--muted);
    padding: 12px 0 10px;
  }
  .label.alt .panel-note { color: var(--orange); }
  .web-band {
    width: 100%;
    height: 48px;
    background: var(--teal);
    color: var(--paper);
    display: flex;
    align-items: center;
    justify-content: center;
    font-size: 18px;
    letter-spacing: 1px;
    text-transform: uppercase;
  }
  .count {
    margin-top: 20px;
    font-size: 36px;
    color: var(--grey);
    text-transform: uppercase;
    letter-spacing: 1px;
  }
</style>
</head>
<body>
  <section class="label">
    <header class="brand-header">
      <div class="brand-mark"></div>
      <div class="brand-name">QUELSTRIDA</div>
      <div class="brand-tagline">Health built on evidence</div>
    </header>
    <div class="header-rule"></div>
    <h1 class="product-name"><span class="word-stress">Stress</span><span class="word-formula">Formula</span></h1>
    <div class="claim-band">
      <div class="claim-title">B- Complex Vitamins</div>
      <div class="claim-detail">With 500 mg Vitamin C per tablet</div>
    </div>
    <div class="panel-note">See side panel for nutrition information</div>
    <div class="rule-orange"></div>
    <div class="web-band">www.quelmira.com</div>
    <div class="rule-orange"></div>
    <div class="count">60 Tablets</div>
  </section>

  <section class="label alt">
    <header class="brand-header">
      <div class="brand-mark"></div>
      <div class="brand-name">QUELSTRIDA</div>
      <div class="brand-tagline">Health built on evidence</div>
    </header>
    <div class="header-rule"></div>
    <h1 class="product-name"><span class="word-stress">Stress</span><span class="word-formula">Formula</span></h1>
    <div class="claim-band">
      <div class="claim-title">B- Complex Vitamins</div>
      <div class="claim-detail">With 500 mg Vitamin C per tablet</div>
    </div>
    <div class="panel-note">See side panel for nutrition information</div>
    <div class="rule-orange"></div>
    <div class="web-band">www.quelmira.com</div>
    <div class="rule-orange"></div>
    <div class="count">60 Tablets</div>
  </section>
</body>
</html>
```